Business card for law firm

Need business card for new law firm. Think confident, authoritative, conservative, but not stuffy or old-fashioned.

Contact Information for Business Card

Content for card - logo (uploaded), plus the following:

Paul Wexbury (larger font)
Managing Partner (larger font, but not as large as name)
Level 9, 41 Tansy Lane
Sydney NSW 2000
Main Tel 02 7346 2190
Direct Tel 02 6273 4415
Email paul@qvlegal.com.au
www.qvlegal.com.au

Letterhead design should include logo plus:
Level 9, 41 Tansy Lane
Sydney NSW 2000
Tel 02 6273 4415
www.qvlegal.com.au

```html
<!DOCTYPE html>
<html lang="en">
<head>
<meta charset="utf-8">
<title>Quayvale Lawyers – Business Card</title>
<link rel="stylesheet" href="https://fonts.googleapis.com/css2?family=Noto+Serif:wght@400;700&family=Cinzel:wght@400&display=swap">
<style>
  :root {
    --page-bg: #e9e9ec;
    --card-front: #f3f3f5;
    --card-back: #262a5a;
    --ink-dark: #1c1c1c;
    --ink-light: #ffffff;
    --ink-soft: #c9cbe0;
  }
  * { box-sizing: border-box; margin: 0; padding: 0; }
  html, body {
    width: 1154px;
    height: 1200px;
    overflow: hidden;
    background: var(--page-bg);
  }
  .sheet {
    position: relative;
    width: 1154px;
    height: 1200px;
  }
  .card {
    position: absolute;
    left: 77px;
    width: 1000px;
    height: 560px;
    border-radius: 26px;
    box-shadow: 0 6px 18px rgba(0,0,0,0.18);
    overflow: hidden;
  }
  .card--front {
    top: 40px;
    background: var(--card-front);
    color: var(--ink-dark);
  }
  .card--back {
    top: 630px;
    background: var(--card-back);
    color: var(--ink-light);
  }

  /* Front */
  .firm-name--large {
    position: absolute;
    top: 220px;
    left: 0;
    width: 100%;
    text-align: center;
    font-family: "Noto Serif", serif;
    font-weight: 400;
    font-size: 74px;
    letter-spacing: 2px;
    text-transform: uppercase;
    line-height: 1;
  }
  .firm-name--large .firm-sub {
    display: block;
    margin-top: 22px;
    font-size: 36px;
    letter-spacing: 30px;
    padding-left: 30px;
  }
  .address-line {
    position: absolute;
    bottom: 44px;
    left: 0;
    width: 100%;
    text-align: center;
    font-family: "Cinzel", serif;
    font-size: 26px;
    letter-spacing: 0.5px;
  }

  /* Back */
  .firm-name--small {
    position: absolute;
    top: 90px;
    left: 70px;
    font-family: "Noto Serif", serif;
    font-weight: 400;
    font-size: 30px;
    line-height: 1;
    text-transform: uppercase;
    text-align: center;
    color: var(--ink-light);
  }
  .firm-name--small .firm-sub {
    display: block;
    margin-top: 6px;
    font-size: 11px;
    letter-spacing: 11px;
    color: var(--ink-soft);
  }
  .contact-block {
    position: absolute;
    left: 60px;
    top: 300px;
    font-family: "Noto Serif", serif;
  }
  .person-name {
    font-size: 44px;
    font-weight: 700;
    line-height: 1.05;
  }
  .person-role {
    font-size: 30px;
    font-weight: 700;
    line-height: 1.1;
    margin-bottom: 26px;
  }
  .phone {
    font-size: 29px;
    line-height: 1.25;
  }
  .phone-label {
    font-size: 17px;
    margin-left: 4px;
  }
  .email {
    font-size: 29px;
    margin-top: 20px;
  }
  .website {
    position: absolute;
    right: 40px;
    top: 190px;
    writing-mode: vertical-rl;
    font-family: "Noto Serif", serif;
    font-size: 28px;
    letter-spacing: 0.5px;
  }
</style>
</head>
<body>
<main class="sheet">
  <section class="card card--front" aria-label="Card front">
    <h1 class="firm-name--large">Quayvale<span class="firm-sub">Lawyers</span></h1>
    <p class="address-line">Level 9 &bull; 41 Tansy Lane &bull; Sydney &bull; NSW &bull; 2000</p>
  </section>

  <section class="card card--back" aria-label="Card back">
    <p class="firm-name--small">Quayvale<span class="firm-sub">Lawyers</span></p>
    <div class="contact-block">
      <h2 class="person-name">Paul Wexbury</h2>
      <p class="person-role">Managing Partner</p>
      <p class="phone">02 7346 2190 <span class="phone-label">(main)</span></p>
      <p class="phone">02 6273 4415 <span class="phone-label">(direct)</span></p>
      <p class="email">paul@qvlegal.com.au</p>
    </div>
    <p class="website">www.qvlegal.com.au</p>
  </section>
</main>
</body>
</html>
```